Veterinary Hospital Brochure - 2 Drafts - 1 Normal and 1 Fun.

Meadowbrook Pet Hospital needs a brochure to promote our veterinary hospital. These will be delivered to local mailboxes. I would like to see atleast 2 submissions from each designer.
One submission conservative and A4 folded DL and another submission more radical and interesting with innovative folding or crazy concepts. Maybe the brochure could be designed to fold into a dog house ?
I want at least one version to be VERY SIMPLE AND INTIMATE.
Our existing website is here: http://furlane.example/ and our new website will look like this: http://trial4.pagemint.example/#home
Please use colors and images from the new website, and information from the old website. The heading font used in the new site is Qorvatype - Otter Tilt Sketchline
I want the brochure to be simple and engaging on first view, and then provide the opportunity to find more information if desired. The brochure needs to be captivating on the outside so people don't throw it away immediately.

We will soon need letterhead, flags, pens, business cards, signs and vouchers so there is the opportunity for more work for the successful designer.

Target Market(s)

Women 25 to 44

Industry/Entity Type

Veterinary

Contact Information for Business Card

Meadowbrook Pet Hospital
14 Marlow Crescent
Tamsworth Vale
NSW 2417
Phone: 02 61938205
Emergency: 0417360592
Fax: 02 83159462
www.meadowbrookvets.example
contact@meadowbrookvets.example

Font styles to use
Script

Requirements
Must have
• Colors from the new website: http://meadowbrookvets.example/ and new logo.
• Information from the old website: http://furlane.example/
• 2 drafts - A normal A4 folded DL flyer and an interesting crazy design.
Nice to have
• VERY SIMPLE
• Subdued
• Intimate
Should not have
• Intense colours
• Red

```html
<!DOCTYPE html>
<html lang="en">
<head>
<meta charset="utf-8">
<title>Meadowbrook Pet Hospital – Trifold Brochure</title>
<link href="https://fonts.googleapis.com/css2?family=Lato:ital,wght@0,400;0,700;0,900;1,400&family=Bree+Serif&family=Oswald:wght@500&display=swap" rel="stylesheet">
<style>
  :root {
    --orange: #ef7a2b;
    --brown: #5b3a1d;
    --green: #8cc63f;
    --green-soft: #b7dc7a;
    --ink: #3a3a3a;
    --paper: #ffffff;
    --paper-shade: #f1f1f1;
    --backdrop: #e4e4e4;
  }
  * { box-sizing: border-box; margin: 0; padding: 0; }
  html, body { width: 1200px; height: 1200px; overflow: hidden; }
  body { background: var(--backdrop); font-family: "Lato", sans-serif; color: var(--ink); }

  .brochure {
    position: absolute; left: 0; top: 176px;
    width: 1200px; height: 848px;
    display: flex; background: var(--paper);
    box-shadow: 0 6px 24px rgba(0,0,0,.15);
  }
  .panel { position: relative; width: 400px; height: 100%; overflow: hidden;
    background: linear-gradient(160deg, var(--paper) 0%, var(--paper-shade) 100%); }
  .panel + .panel { border-left: 1px solid #e2e2e2; }

  .photo { position: absolute; }
  .swoosh { position: absolute; left: 0; width: 400px; }

  /* Left panel */
  .photo--reception { left: 0; top: 0; width: 400px; height: 180px;
    background: linear-gradient(135deg, #e9e3d3, #b8643a 60%, #7a4a2b); }
  .services-title { position: absolute; top: 200px; right: 56px;
    font: 900 15px "Lato", sans-serif; color: var(--orange); letter-spacing: .5px; }
  .services { position: absolute; top: 232px; left: 40px; right: 30px;
    display: flex; gap: 22px; }
  .services ul { list-style: none; flex: 1; }
  .services li { font: italic 400 13.5px/19px "Lato", sans-serif; display: flex; gap: 6px; }
  .services li svg { flex: none; margin-top: 5px; }
  .photo--pets { left: 40px; top: 430px; width: 320px; height: 300px; border-radius: 8px;
    background: radial-gradient(circle at 65% 45%, #c98e55, #e9d3b6 55%, var(--paper) 80%); }
  .url--left { position: absolute; bottom: 36px; left: 0; right: 0; text-align: center;
    font: 700 14px "Lato", sans-serif; letter-spacing: 1.5px; color: var(--ink); }

  /* Middle panel */
  .about { position: absolute; top: 40px; left: 40px; right: 36px;
    font: italic 400 14px/19px "Lato", sans-serif; }
  .about p { margin-bottom: 6px; }
  .about ul { list-style: none; }
  .about li { display: flex; gap: 8px; }
  .about li::before { content: ""; width: 9px; height: 9px; margin-top: 5px; flex: none;
    border: 2px solid var(--orange); border-radius: 50%; }
  .brand { font: 500 30px/1 "Oswald", sans-serif; color: var(--brown); letter-spacing: 1px;
    text-transform: uppercase; text-align: center; }
  .brand--middle { position: absolute; top: 226px; left: 0; right: 0; }
  .brand small { display: block; font-size: 19px; margin-bottom: 4px; }
  .contact { position: absolute; top: 318px; left: 58px; list-style: none;
    font: 400 14px/24px "Lato", sans-serif; }
  .contact li { display: flex; align-items: center; gap: 10px; }
  .contact .dot { width: 12px; height: 12px; border-radius: 50%; background: var(--ink); flex: none; }
  .map { left: 0; top: 470px; width: 400px; height: 378px;
    background: linear-gradient(160deg, #eef0e6, #e0e4d6 60%, #eaeadf); }

  /* Right panel */
  .brand--right { position: absolute; top: 98px; left: 0; right: 0; }
  .photo--building { left: 0; top: 200px; width: 400px; height: 360px;
    background: linear-gradient(180deg, #c9d4dd 0%, #dfe4e8 30%, #8b4a35 55%, #6a3a2a 80%, #8e8a7e 100%); }
  .welcome { position: absolute; top: 612px; left: 0; right: 0; text-align: center; }
  .welcome h1 { font: 400 52px/1 "Bree Serif", serif; color: var(--orange); }
  .welcome h2 { font: 500 22px/1.2 "Oswald", sans-serif; color: var(--brown);
    letter-spacing: 1.5px; margin-top: 4px; }
  .url--right { position: absolute; bottom: 82px; left: 0; right: 0; text-align: center;
    font: 700 15px "Lato", sans-serif; letter-spacing: 2px; color: var(--brown); }
</style>
</head>
<body>
<main class="brochure">

  <section class="panel panel--services">
    <div class="photo photo--reception" role="img" aria-label="Photo of a cat sitting on the reception counter beside an award"></div>
    <svg class="swoosh" style="top:130px" height="70" viewBox="0 0 400 70" aria-hidden="true">
      <path d="M0 40 C120 70 260 10 400 0 L400 20 C260 30 120 80 0 60Z" fill="var(--green)"/>
      <path d="M0 52 C130 80 270 22 400 12 L400 70 L0 70Z" fill="var(--paper)"/>
      <path d="M0 50 C130 78 270 20 400 10 L400 16 C270 28 130 84 0 58Z" fill="var(--brown)"/>
    </svg>
    <h3 class="services-title">SERVICES</h3>
    <div class="services">
      <ul>
        <li><svg width="10" height="8" viewBox="0 0 10 8"><path d="M1 4l3 3 5-6" fill="none" stroke="var(--green)" stroke-width="2"/></svg>Vaccinations</li>
        <li><svg width="10" height="8" viewBox="0 0 10 8"><path d="M1 4l3 3 5-6" fill="none" stroke="var(--green)" stroke-width="2"/></svg>Vaccination Reminders</li>
        <li><svg width="10" height="8" viewBox="0 0 10 8"><path d="M1 4l3 3 5-6" fill="none" stroke="var(--green)" stroke-width="2"/></svg>Companion Animal De-sexing</li>
        <li><svg width="10" height="8" viewBox="0 0 10 8"><path d="M1 4l3 3 5-6" fill="none" stroke="var(--green)" stroke-width="2"/></svg>Emergency Surgery</li>
        <li><svg width="10" height="8" viewBox="0 0 10 8"><path d="M1 4l3 3 5-6" fill="none" stroke="var(--green)" stroke-width="2"/></svg>Dental</li>
        <li><svg width="10" height="8" viewBox="0 0 10 8"><path d="M1 4l3 3 5-6" fill="none" stroke="var(--green)" stroke-width="2"/></svg>Caeserian</li>
        <li><svg width="10" height="8" viewBox="0 0 10 8"><path d="M1 4l3 3 5-6" fill="none" stroke="var(--green)" stroke-width="2"/></svg>Behaviour Consults</li>
        <li><svg width="10" height="8" viewBox="0 0 10 8"><path d="M1 4l3 3 5-6" fill="none" stroke="var(--green)" stroke-width="2"/></svg>Aged Care Consults</li>
      </ul>
      <ul>
        <li><svg width="10" height="8" viewBox="0 0 10 8"><path d="M1 4l3 3 5-6" fill="none" stroke="var(--green)" stroke-width="2"/></svg>Nutrition Advice</li>
        <li><svg width="10" height="8" viewBox="0 0 10 8"><path d="M1 4l3 3 5-6" fill="none" stroke="var(--green)" stroke-width="2"/></svg>Flea Treatments</li>
        <li><svg width="10" height="8" viewBox="0 0 10 8"><path d="M1 4l3 3 5-6" fill="none" stroke="var(--green)" stroke-width="2"/></svg>Radiology</li>
        <li><svg width="10" height="8" viewBox="0 0 10 8"><path d="M1 4l3 3 5-6" fill="none" stroke="var(--green)" stroke-width="2"/></svg>Ultrasound</li>
        <li><svg width="10" height="8" viewBox="0 0 10 8"><path d="M1 4l3 3 5-6" fill="none" stroke="var(--green)" stroke-width="2"/></svg>Routine Blood Tests</li>
        <li><svg width="10" height="8" viewBox="0 0 10 8"><path d="M1 4l3 3 5-6" fill="none" stroke="var(--green)" stroke-width="2"/></svg>Orthopaedic Surgery</li>
        <li><svg width="10" height="8" viewBox="0 0 10 8"><path d="M1 4l3 3 5-6" fill="none" stroke="var(--green)" stroke-width="2"/></svg>Cruciate Repair</li>
        <li><svg width="10" height="8" viewBox="0 0 10 8"><path d="M1 4l3 3 5-6" fill="none" stroke="var(--green)" stroke-width="2"/></svg>Grieving Support</li>
        <li><svg width="10" height="8" viewBox="0 0 10 8"><path d="M1 4l3 3 5-6" fill="none" stroke="var(--green)" stroke-width="2"/></svg>Skin Treatments</li>
      </ul>
    </div>
    <div class="photo photo--pets" role="img" aria-label="Photo of a happy dog lying beside a grey kitten"></div>
    <p class="url--left">www.furlane.example</p>
  </section>

  <section class="panel panel--contact">
    <div class="about">
      <p>Meadowbrook Pet Hospital is a Companion Animal Veterinary Hospital in Tamsworth Vale committed to providing excellent care for loved pets and their owners.</p>
      <p>To achieve this we:</p>
      <ul>
        <li>Provide a welcoming environment.</li>
        <li>Treat all patients and owners as important.</li>
        <li>Educate owners to help prevent illness.</li>
        <li>When illness occurs, treat with the latest equipment and techniques.</li>
      </ul>
    </div>
    <p class="brand brand--middle"><small>Meadowbrook Pet</small>Hospital</p>
    <ul class="contact">
      <li><svg width="12" height="14" viewBox="0 0 12 14"><path d="M6 0a5 5 0 015 5c0 4-5 9-5 9S1 9 1 5a5 5 0 015-5z" fill="var(--ink)"/><circle cx="6" cy="5" r="2" fill="#fff"/></svg>14 Marlow Crescent Tamsworth Vale NSW 2417.</li>
      <li><svg width="12" height="12" viewBox="0 0 12 12"><path d="M2 1l3 0 1 3-2 1c1 2 2 3 4 4l1-2 3 1 0 3c-6 0-10-4-10-10z" fill="var(--ink)"/></svg>02 6193 8205</li>
      <li><svg width="12" height="12" viewBox="0 0 12 12"><rect x="1" y="4" width="10" height="7" fill="var(--ink)"/><rect x="3" y="1" width="6" height="4" fill="none" stroke="var(--ink)"/></svg>61938207</li>
      <li><svg width="12" height="10" viewBox="0 0 12 10"><rect x=".5" y=".5" width="11" height="9" fill="none" stroke="var(--ink)"/><path d="M.5 .5l5.5 5 5.5-5" fill="none" stroke="var(--ink)"/></svg>contact@furlane.example</li>
      <li><svg width="12" height="12" viewBox="0 0 12 12"><circle cx="6" cy="6" r="5.5" fill="none" stroke="var(--ink)"/><path d="M.5 6h11M6 .5c-3 3-3 8 0 11M6 .5c3 3 3 8 0 11" fill="none" stroke="var(--ink)"/></svg>www.furlane.example</li>
      <li><span class="dot"></span>Meadowbrook PetHospital</li>
    </ul>
    <svg class="swoosh" style="top:440px;z-index:2" height="60" viewBox="0 0 400 60" aria-hidden="true">
      <path d="M0 0 C80 40 240 40 400 30 L400 60 L0 60Z" fill="var(--green)"/>
      <path d="M0 14 C90 52 240 50 400 42 L400 60 L0 60Z" fill="var(--brown)"/>
      <path d="M0 22 C90 58 240 56 400 50 L400 60 L0 60Z" fill="var(--map-edge, #e6e9dc)"/>
    </svg>
    <div class="photo map" role="img" aria-label="Street map of Tamsworth Vale with the hospital location marked"></div>
  </section>

  <section class="panel panel--cover">
    <p class="brand brand--right"><small>Meadowbrook Pet</small>Hospital</p>
    <div class="photo photo--building" role="img" aria-label="Photo of the red brick hospital building with a VET sign and timber gate"></div>
    <svg class="swoosh" style="top:520px" height="70" viewBox="0 0 400 70" aria-hidden="true">
      <path d="M0 0 C120 40 280 60 400 40 L400 70 L0 70Z" fill="var(--paper)"/>
      <path d="M0 0 C120 40 280 60 400 40 L400 48 C280 66 120 50 0 10Z" fill="var(--green)"/>
      <path d="M0 10 C120 50 280 68 400 48 L400 54 C280 74 120 58 0 18Z" fill="var(--brown)"/>
    </svg>
    <div class="welcome">
      <h1>Welcome to</h1>
      <h2>MEADOWBROOK PET HOSPITAL</h2>
    </div>
    <svg class="swoosh" style="bottom:0" height="110" viewBox="0 0 400 110" aria-hidden="true">
      <path d="M0 10 C140 60 280 70 400 50 L400 110 L0 110Z" fill="var(--green)"/>
      <path d="M0 0 C140 50 280 60 400 40 L400 46 C280 66 140 56 0 6Z" fill="var(--brown)"/>
    </svg>
    <p class="url--right">www.furlane.example</p>
  </section>

</main>
</body>
</html>
```